Marwick home cleaning

Design a car wrap for a home cleaning company. The name company Marwick Home cleaning. slogan " we clean, you relax" our instgram is @marwickhc

Target Market(s)

Homes, apts, offices, villas

Industry/Entity Type

Home cleaning

Colors
0054AA
0677BA
7BADD7
CADEEF
E8F1F8
0094D4
00A9DD
6FCCEA
C7EBF8
E9F6FB
FFC000
F8CF3A
FAE287
FDF2CF
FEFAEE

Requirements
Must have
• Home cleaning,
Nice to have
• i want simple design straign not too much wrap, an image clearly tells you about the company along with sname slogan and contact details phone, instgram, website

```html
<!DOCTYPE html>
<html lang="en">
<head>
<meta charset="utf-8">
<title>Marwick Home cleaning – vehicle wrap</title>
<link rel="stylesheet" href="https://fonts.googleapis.com/css2?family=Montserrat:wght@400;500;600;700&family=Cairo:wght@500;700&display=swap">
<style>
  :root{
    --navy:#0054AA;
    --blue:#0677BA;
    --sky:#7BADD7;
    --mist:#CADEEF;
    --ice:#E8F1F8;
    --cyan:#0094D4;
    --aqua:#6FCCEA;
    --foam:#E9F6FB;
    --paint:#F4F6F8;
    --trim:#2B2F33;
    --grey:#5B6670;
    --page:#FFFFFF;
  }
  *{box-sizing:border-box;margin:0;padding:0}
  html,body{width:1200px;height:1200px;overflow:hidden;background:var(--page)}
  body{position:relative;font-family:"Montserrat",Arial,sans-serif}
  .wrap-panel{position:absolute;display:block}
  .side-a{left:50px;top:40px;width:1100px;height:300px}
  .side-b{left:50px;top:380px;width:1100px;height:300px}
  .rear-a{left:50px;top:740px;width:520px;height:400px}
  .rear-b{left:630px;top:740px;width:520px;height:400px}
  .brand{font-family:"Montserrat",Arial,sans-serif;font-weight:600;fill:var(--navy);letter-spacing:1px}
  .brand-sub{font-family:"Montserrat",Arial,sans-serif;font-weight:500;fill:var(--grey)}
  .arabic{font-family:"Cairo",Arial,sans-serif;font-weight:700}
  .phone{font-family:"Montserrat",Arial,sans-serif;font-weight:700;fill:var(--navy)}
  .web{font-family:"Montserrat",Arial,sans-serif;font-weight:500;fill:var(--blue)}
  .slogan{font-family:"Montserrat",Arial,sans-serif;font-weight:600;fill:#fff}
  .handle{font-family:"Montserrat",Arial,sans-serif;font-weight:500;fill:#fff}
</style>
</head>
<body>

<!-- Side layout: curved rear sweep -->
<svg class="wrap-panel side-a" viewBox="0 0 1100 300" role="group" aria-label="Side wrap layout, curved sweep">
  <defs>
    <linearGradient id="sweepA" x1="0" y1="0" x2="1" y2="0">
      <stop offset="0" stop-color="#7BADD7"/>
      <stop offset="1" stop-color="#0677BA"/>
    </linearGradient>
    <radialGradient id="bubbleSoft" cx="0.5" cy="0.5" r="0.5">
      <stop offset="0" stop-color="#E8F1F8" stop-opacity="0.9"/>
      <stop offset="1" stop-color="#CADEEF" stop-opacity="0"/>
    </radialGradient>
  </defs>
  <rect class="body-paint" x="0" y="0" width="1100" height="300" rx="18" fill="var(--paint)"/>
  <path class="rear-sweep" d="M870 0 H1082 Q1100 0 1100 18 V282 Q1100 300 1082 300 H810 C880 210 860 90 870 0 Z" fill="url(#sweepA)"/>
  <rect class="squeegee-art" x="900" y="40" width="170" height="170" rx="16" fill="#CADEEF" opacity="0.55" role="img" aria-label="Illustration of a squeegee wiping with soap bubbles"/>
  <ellipse class="bubble-art" cx="200" cy="110" rx="100" ry="65" fill="url(#bubbleSoft)" role="img" aria-label="Soap bubble illustration"/>
  <text class="brand" x="300" y="140" font-size="50">MARWICK</text>
  <text class="brand-sub" x="302" y="168" font-size="17">Cleaning Services</text>
  <text class="arabic" x="500" y="196" font-size="17" fill="var(--navy)" text-anchor="end">مارويك لخدمات التنظيف</text>
  <text class="phone" x="600" y="124" font-size="22">+971 50 218 7409</text>
  <text class="web" x="600" y="148" font-size="14">www.marwickcleaninguae.com</text>
  <rect class="accent-line" x="0" y="232" width="820" height="4" fill="var(--cyan)"/>
  <rect class="trim-band" x="0" y="244" width="805" height="56" fill="var(--trim)"/>
  <text class="slogan" x="300" y="278" font-size="16">we clean, you relax</text>
  <rect x="480" y="262" width="2" height="22" fill="#fff"/>
  <text class="arabic" x="496" y="280" font-size="16" fill="#fff">عندنا الترتيب</text>
  <circle cx="632" cy="272" r="9" fill="none" stroke="#fff" stroke-width="2"/>
  <text class="handle" x="650" y="278" font-size="15">@marwickhc</text>
</svg>

<!-- Side layout: diagonal stripes -->
<svg class="wrap-panel side-b" viewBox="0 0 1100 300" role="group" aria-label="Side wrap layout, diagonal stripes">
  <defs>
    <linearGradient id="sweepB" x1="0" y1="0" x2="1" y2="1">
      <stop offset="0" stop-color="#6FCCEA"/>
      <stop offset="1" stop-color="#0677BA"/>
    </linearGradient>
    <radialGradient id="bubbleSoftB" cx="0.5" cy="0.5" r="0.5">
      <stop offset="0" stop-color="#E8F1F8" stop-opacity="0.9"/>
      <stop offset="1" stop-color="#CADEEF" stop-opacity="0"/>
    </radialGradient>
  </defs>
  <rect class="body-paint" x="0" y="0" width="1100" height="300" rx="18" fill="var(--paint)"/>
  <path class="stripe" d="M880 0 H920 L840 300 H800 Z" fill="var(--sky)"/>
  <path class="stripe" d="M935 0 H970 L890 300 H855 Z" fill="var(--blue)"/>
  <path class="rear-block" d="M985 0 H1082 Q1100 0 1100 18 V282 Q1100 300 1082 300 H905 Z" fill="url(#sweepB)"/>
  <rect class="squeegee-art" x="985" y="60" width="95" height="160" rx="14" fill="#CADEEF" opacity="0.55" role="img" aria-label="Illustration of a squeegee wiping with soap bubbles"/>
  <ellipse class="bubble-art" cx="200" cy="110" rx="100" ry="65" fill="url(#bubbleSoftB)" role="img" aria-label="Soap bubble illustration"/>
  <text class="brand" x="300" y="140" font-size="50">MARWICK</text>
  <text class="brand-sub" x="302" y="168" font-size="17">Cleaning Services</text>
  <text class="arabic" x="500" y="196" font-size="17" fill="var(--navy)" text-anchor="end">مارويك لخدمات التنظيف</text>
  <text class="phone" x="600" y="124" font-size="22">+971 50 218 7409</text>
  <text class="web" x="600" y="148" font-size="14">www.marwickcleaninguae.com</text>
  <rect class="accent-line" x="0" y="232" width="800" height="4" fill="var(--cyan)"/>
  <rect class="trim-band" x="0" y="244" width="790" height="56" fill="var(--trim)"/>
  <text class="slogan" x="300" y="278" font-size="16">we clean, you relax</text>
  <rect x="480" y="262" width="2" height="22" fill="#fff"/>
  <text class="arabic" x="496" y="280" font-size="16" fill="#fff">عندنا الترتيب</text>
  <circle cx="632" cy="272" r="9" fill="none" stroke="#fff" stroke-width="2"/>
  <text class="handle" x="650" y="278" font-size="15">@marwickhc</text>
</svg>

<!-- Rear layout with name -->
<svg class="wrap-panel rear-a" viewBox="0 0 520 400" role="group" aria-label="Rear wrap layout with name">
  <defs>
    <linearGradient id="rearFill" x1="0" y1="0" x2="0" y2="1">
      <stop offset="0" stop-color="#0094D4"/>
      <stop offset="1" stop-color="#0054AA"/>
    </linearGradient>
  </defs>
  <rect x="0" y="0" width="520" height="400" rx="22" fill="url(#rearFill)"/>
  <rect class="window" x="60" y="30" width="400" height="110" rx="14" fill="var(--trim)"/>
  <rect class="bubble-art" x="330" y="160" width="170" height="100" rx="14" fill="#6FCCEA" opacity="0.35" role="img" aria-label="Soap bubble illustration"/>
  <text x="40" y="200" font-size="40" font-weight="600" fill="#fff" letter-spacing="1">MARWICK</text>
  <text x="42" y="222" font-size="13" font-weight="500" fill="#fff">Cleaning Services</text>
  <text class="arabic" x="178" y="242" font-size="13" fill="#fff" text-anchor="end">مارويك لخدمات التنظيف</text>
  <text x="40" y="290" font-size="19" font-weight="700" fill="#fff">+971 50 218 7409</text>
  <rect x="232" y="274" width="2" height="20" fill="#fff"/>
  <text x="246" y="289" font-size="13" font-weight="500" fill="#fff">www.marwickcleaninguae.com</text>
  <rect x="0" y="320" width="520" height="80" fill="var(--trim)"/>
  <text class="slogan" x="40" y="367" font-size="19">we clean, you relax</text>
  <rect x="262" y="348" width="2" height="24" fill="#fff"/>
  <text class="arabic" x="280" y="369" font-size="19" fill="#fff">عندنا الترتيب</text>
</svg>

<!-- Rear layout, contact only -->
<svg class="wrap-panel rear-b" viewBox="0 0 520 400" role="group" aria-label="Rear wrap layout, contact only">
  <defs>
    <linearGradient id="rearFillB" x1="0" y1="0" x2="0" y2="1">
      <stop offset="0" stop-color="#6FCCEA"/>
      <stop offset="1" stop-color="#0677BA"/>
    </linearGradient>
  </defs>
  <rect x="0" y="0" width="520" height="400" rx="22" fill="url(#rearFillB)"/>
  <rect class="window" x="60" y="30" width="400" height="110" rx="14" fill="var(--trim)"/>
  <rect class="bubble-art" x="30" y="160" width="460" height="90" rx="14" fill="#E9F6FB" opacity="0.3" role="img" aria-label="Soap bubble illustration"/>
  <text x="40" y="290" font-size="19" font-weight="700" fill="#fff">+971 50 218 7409</text>
  <rect x="232" y="274" width="2" height="20" fill="#fff"/>
  <text x="246" y="289" font-size="13" font-weight="500" fill="#fff">www.marwickcleaninguae.com</text>
  <rect x="0" y="320" width="520" height="80" fill="var(--trim)"/>
  <text class="slogan" x="40" y="367" font-size="19">we clean, you relax</text>
  <rect x="262" y="348" width="2" height="24" fill="#fff"/>
  <text class="arabic" x="280" y="369" font-size="19" fill="#fff">عندنا الترتيب</text>
</svg>

</body>
</html>
```